KirvaLume a new start up looking for packaging design for it's organic Cold pressed Peanut oil.

We require a labelling design for a new company based in the UK called ''KirvaLume''. We will be launching Organic cold pressed peanut oil. We would like a design that is simple yet very catchy and not boring.

Target Market(s)
General consumers and healthy eaters, Vegan friendly

Colors
Designer to choose colors to be used in the design.

Must have
• Refer to Packaging document information for labelling.
• Type of bottle 250 ML Tasbel bottle (refer to Bottle Picture doc.)
• Must have the "KirvaLume" logo stamped somewhere on the front of the package (refer to the Logo document)
• Sleek and appetising design
• Neutral colors possible accents with logo colors
• Claims: Organic, Vegan, High in Monounsaturated fat, High in Poly-unsaturated fat(all this in front of the package)
• Made in the uk logo, and EU organic logo
• Social Media Icons (Instagram,Facebook) as well as website (Kirvalume.co.uk)
• Space reserved at the back of the package for barcode and best before date to be printed on.
Be nice to have: picture of the product on the background if possible

Need extra days to review

Target Market(s)

Font styles to use
Serif
Sans Serif
Decorative
Script

Requirements
Must have

• • Refer to Packaging document information for labelling.

```html
<!DOCTYPE html>
<html lang="en">
<head>
<meta charset="utf-8">
<title>KirvaLume Peanut Oil – Labels</title>
<link rel="stylesheet" href="https://fonts.googleapis.com/css2?family=Archivo+Black&family=Cabin:wght@400;600&display=swap">
<style>
  :root {
    --page: #ffffff;
    --silver-light: #e6e6e6;
    --silver-dark: #c9c9c9;
    --ink: #1e1a18;
    --cocoa: #4a2a26;
    --cocoa-deep: #3a1f1c;
    --splash: #5a1e16;
    --tan: #c9a07a;
    --cream: #f1ebe6;
    --white: #ffffff;
  }
  html, body {
    margin: 0;
    width: 1200px;
    height: 1200px;
    overflow: hidden;
    background: var(--page);
  }
  .canvas {
    position: relative;
    width: 1200px;
    height: 1200px;
  }
  .label {
    position: absolute;
    top: 60px;
    width: 360px;
    height: 1080px;
  }
  .label--back { left: 180px; }
  .label--front { left: 660px; }

  .body-text { font-family: "Cabin", sans-serif; fill: var(--ink); }
  .heading { font-family: "Cabin", sans-serif; font-weight: 600; fill: var(--ink); }
  .allergy-text { font-weight: 600; }
  .product-name { font-family: "Archivo Black", sans-serif; fill: var(--cocoa); letter-spacing: 2px; }
  .brand-name { font-family: "Cabin", sans-serif; font-weight: 600; fill: var(--cocoa); }
  .volume { font-family: "Cabin", sans-serif; fill: var(--cream); }
  .claim { font-family: "Cabin", sans-serif; fill: var(--cream); }
  .claim-box { fill: none; stroke: var(--tan); stroke-width: 1.5; }
  .tan { fill: var(--tan); }
  .white { fill: var(--white); }
</style>
</head>
<body>
<main class="canvas">

  <!-- Back label -->
  <svg class="label label--back" viewBox="0 0 360 1080" xmlns="http://www.w3.org/2000/svg" aria-label="Back label">
    <defs>
      <linearGradient id="silverGrad" x1="0" y1="0" x2="1" y2="0">
        <stop offset="0" stop-color="var(--silver-dark)"/>
        <stop offset="0.5" stop-color="var(--silver-light)"/>
        <stop offset="1" stop-color="var(--silver-dark)"/>
      </linearGradient>
      <linearGradient id="splashArea" x1="0" y1="0" x2="1" y2="1">
        <stop offset="0" stop-color="var(--splash)" stop-opacity="0.12"/>
        <stop offset="1" stop-color="var(--splash)" stop-opacity="0.35"/>
      </linearGradient>
    </defs>
    <rect class="label-base" width="360" height="1080" fill="url(#silverGrad)"/>

    <text class="heading" x="19" y="42" font-size="30">Nutrition Information</text>
    <g class="nutrition-table body-text" font-size="18">
      <text x="19" y="76">Typical values</text><text x="344" y="76" text-anchor="end">per 100g</text>
      <text x="19" y="103">Energy</text><text x="344" y="103" text-anchor="end">kJ896/kCal3685</text>
      <text x="19" y="130">Fat</text><text x="344" y="130" text-anchor="end">100g</text>
      <text x="19" y="157">Of which Saturated</text><text x="344" y="157" text-anchor="end">19.7g</text>
      <text x="19" y="184">Mono-unsaturated</text><text x="344" y="184" text-anchor="end">36.4g</text>
      <text x="19" y="211">Poly-unsaturated</text><text x="344" y="211" text-anchor="end">43.4g</text>
      <text x="19" y="238">Protein</text><text x="344" y="238" text-anchor="end">0.1g</text>
      <text x="19" y="265">Carbohydrate</text><text x="344" y="265" text-anchor="end">&lt;0.5g</text>
      <text x="19" y="292">Of which sugar</text><text x="344" y="292" text-anchor="end">&lt;0.1g</text>
      <text x="19" y="319">Fibre</text><text x="344" y="319" text-anchor="end">&lt;0.5</text>
    </g>

    <text class="heading" x="19" y="378" font-size="30">Ingredients</text>
    <text class="body-text" x="19" y="402" font-size="18">100% Organic peanut oil</text>

    <text class="body-text" x="19" y="466" font-size="17">Allergy advice:</text>
    <g class="allergy-text body-text" font-size="11.5">
      <text x="19" y="484">Packed on premises that handles cereals, nuts</text>
      <text x="19" y="498">(including peanuts), soya, sesame and products</text>
      <text x="19" y="512">containing gluten.</text>
    </g>

    <rect class="decor-area" role="img" aria-label="Decorative brown ink brush stroke with splatter drops"
          x="0" y="545" width="360" height="440" fill="url(#splashArea)"/>
  </svg>

  <!-- Front label -->
  <svg class="label label--front" viewBox="0 0 360 1080" xmlns="http://www.w3.org/2000/svg" aria-label="Front label">
    <defs>
      <linearGradient id="cocoaGrad" x1="0" y1="0" x2="1" y2="0">
        <stop offset="0" stop-color="var(--cocoa-deep)"/>
        <stop offset="0.5" stop-color="var(--cocoa)"/>
        <stop offset="1" stop-color="var(--cocoa-deep)"/>
      </linearGradient>
      <linearGradient id="frontDecorArea" x1="0" y1="0" x2="0" y2="1">
        <stop offset="0" stop-color="#2c1412" stop-opacity="0.1"/>
        <stop offset="1" stop-color="#2c1412" stop-opacity="0.35"/>
      </linearGradient>
    </defs>
    <rect class="label-base" width="360" height="1080" fill="url(#cocoaGrad)"/>

    <rect class="decor-area" role="img" aria-label="Faint dark ink brush stroke decoration"
          x="0" y="640" width="360" height="300" fill="url(#frontDecorArea)"/>

    <!-- Vertical name band and badge -->
    <rect class="tan" x="117" y="0" width="136" height="560"/>
    <rect class="white" x="128" y="0" width="114" height="560"/>
    <circle class="tan" cx="185" cy="564" r="150"/>
    <circle class="white" cx="185" cy="564" r="139"/>
    <rect class="white" x="128" y="380" width="114" height="60"/>

    <text class="product-name" font-size="62" text-anchor="middle"
          transform="translate(207 215) rotate(-90)">PEANUT OIL</text>

    <text class="brand-name" x="185" y="580" font-size="46" text-anchor="middle">KirvaLume</text>

    <text class="volume" x="185" y="800" font-size="40" text-anchor="middle">250 ML</text>

    <rect class="tan" x="0" y="944" width="360" height="8"/>

    <g class="claims">
      <rect class="claim-box" x="110" y="975" width="12" height="12"/>
      <text class="claim" x="132" y="986" font-size="12">Organic</text>
      <rect class="claim-box" x="110" y="997" width="12" height="12"/>
      <text class="claim" x="132" y="1008" font-size="12">Vegan</text>
      <rect class="claim-box" x="110" y="1019" width="12" height="12"/>
      <text class="claim" x="132" y="1030" font-size="12">High in Monounsaturated fat</text>
      <rect class="claim-box" x="110" y="1041" width="12" height="12"/>
      <text class="claim" x="132" y="1052" font-size="12">High in Poly-unsaturated fat</text>
    </g>
  </svg>

</main>
</body>
</html>
```